THE HEADLAND AT TALL PINE HUDSON RIVER WATERFRONT LAND

crisp clear business cards on wood stock or thick paper with large font with a river otter logo, PERSONAL INFO ON ONE SIDE, PROJECT INFO ON THE OTHER SIDE
Updates

I don’t have a logo. Just thought that a photo of a river otter would look appealing.

Target Market(s)

Buyers and realtors

Industry/Entity Type

Real Estate Development

Contact Information for Business Card

MARTIN KOWALCZYK
607-318-5942 (Call or Text)
STONE MEADOW LLC PRINCIPAL

RQVWFIELD@NORVAMAIL.NET

Font styles to use
Sans Serif

Colors
fbfdfe
0792cd
00a990
fbed22
ec1f27

Requirements
Must have
• LARGE FONT, ROUNDED EDGES,
Nice to have
• ON THE BACK SIDE :
• THE HEADLAND AT TALL PINE
• HUDSON RIVER WATERFRONT LAND
• 2 TO 67 ACRES---READY TO BUILD
• PRICED TO SELL!

```html
<!DOCTYPE html>
<html lang="en">
<head>
<meta charset="utf-8">
<title>Stone Meadow LLC – Business Card</title>
<link href="https://fonts.googleapis.com/css2?family=Montserrat:wght@500;600&family=Work+Sans:wght@400;500&display=swap" rel="stylesheet">
<style>
  :root {
    --bg: #1c1c1c;
    --card-dark: #232323;
    --card-light: #fbfdfe;
    --blue: #0792cd;
    --ink: #4a4a4a;
    --white: #f4f4f4;
  }
  * { box-sizing: border-box; margin: 0; padding: 0; }
  html, body {
    width: 1200px; height: 900px; overflow: hidden;
    background: var(--bg);
  }
  .stage {
    width: 1200px; height: 900px;
    display: flex; flex-direction: column; align-items: center; justify-content: center;
    gap: 40px;
  }
  .card {
    width: 700px; height: 400px;
    border-radius: 18px;
    position: relative;
    box-shadow: 0 12px 30px rgba(0,0,0,.45);
  }
  .card--back {
    background: linear-gradient(135deg, #1e1e1e 0%, #2c2c2c 70%, #353535 100%);
    display: flex; flex-direction: column; align-items: center; justify-content: center;
    gap: 48px;
  }
  .card--front {
    background: var(--card-light);
  }
  .company-name {
    font-family: "Montserrat", sans-serif;
    font-weight: 600;
    color: var(--blue);
    letter-spacing: 4px;
    font-size: 40px;
  }
  .project-info {
    font-family: "Montserrat", sans-serif;
    font-weight: 500;
    color: var(--white);
    font-size: 15px;
    letter-spacing: 1px;
    text-align: center;
    line-height: 1.6;
  }
  .card--front .company-name {
    position: absolute; top: 70px; left: 0; right: 0; text-align: center;
  }
  .contact-row {
    position: absolute; top: 190px; left: 60px; right: 40px;
    display: flex; align-items: center;
  }
  .person { text-align: right; width: 270px; }
  .person-name {
    font-family: "Montserrat", sans-serif; font-weight: 600;
    color: var(--blue); font-size: 27px; line-height: 1.1;
  }
  .person-title {
    font-family: "Work Sans", sans-serif; color: var(--ink); font-size: 19px;
  }
  .divider {
    width: 2px; height: 56px; background: var(--blue); margin: 0 26px;
  }
  .details { font-family: "Work Sans", sans-serif; color: var(--ink); font-size: 19px; line-height: 1.5; }
  .detail { display: flex; align-items: center; gap: 10px; }
  .detail svg { width: 14px; height: 14px; flex: none; }
  .address {
    position: absolute; bottom: 70px; left: 0; right: 0; text-align: center;
    font-family: "Work Sans", sans-serif; color: var(--ink); font-size: 20px; letter-spacing: .5px;
  }
</style>
</head>
<body>
<main class="stage">
  <section class="card card--back">
    <h1 class="company-name">STONE MEADOW LLC</h1>
    <p class="project-info">
      THE HEADLAND AT TALL PINE | HUDSON RIVER WATERFRONT LAND<br>
      2 TO 67 ACRES---READY TO BUILD &nbsp;| PRICED TO SELL!
    </p>
  </section>

  <section class="card card--front">
    <h2 class="company-name">STONE MEADOW LLC</h2>
    <div class="contact-row">
      <div class="person">
        <p class="person-name">MARTIN KOWALCZYK</p>
        <p class="person-title">Principal</p>
      </div>
      <div class="divider"></div>
      <div class="details">
        <p class="detail">
          <svg viewBox="0 0 24 24" aria-hidden="true"><path fill="#0792cd" d="M6.6 10.8a15 15 0 0 0 6.6 6.6l2.2-2.2a1 1 0 0 1 1-.25 11.4 11.4 0 0 0 3.6.57 1 1 0 0 1 1 1V20a1 1 0 0 1-1 1A17 17 0 0 1 3 4a1 1 0 0 1 1-1h3.5a1 1 0 0 1 1 1c0 1.25.2 2.45.57 3.6a1 1 0 0 1-.25 1z"/></svg>
          607-318-5942
        </p>
        <p class="detail">
          <svg viewBox="0 0 24 24" aria-hidden="true"><rect x="3" y="5" width="18" height="14" rx="2" fill="none" stroke="#0792cd" stroke-width="2"/><path d="M3 7l9 6 9-6" fill="none" stroke="#0792cd" stroke-width="2"/></svg>
          rqvwfield@norvamail.net
        </p>
      </div>
    </div>
    <p class="address">214 Alder Lane, Riverton, NY, 12083</p>
  </section>
</main>
</body>
</html>
```